" É uma clínica especializada em atendimentos nas disfunções do assoalho pélvico em homens e mulheres. Atendemos disfunções miccionais como incontinência urinária. Disfunções sexuais femininas ( dispareunia e vaginismo); e nos homens ( disfunção erétil e ejaculação rápida) Além de dor pélvica crônica. "

```html
<!DOCTYPE html>
<html lang="pt-BR">
<head>
<meta charset="utf-8">
<title>Helena Moraes – Fisioterapia Pélvica</title>
<link href="https://fonts.googleapis.com/css2?family=PT+Serif:ital,wght@0,400;0,700;1,400;1,700&display=swap" rel="stylesheet">
<style>
  :root {
    --teal: #17977f;
    --teal-dark: #0d7a66;
    --teal-light: #7cc9b8;
    --paper: #ffffff;
    --stage: #d9dadb;
    --ink-soft: #e8f5f1;
  }
  * { margin: 0; padding: 0; box-sizing: border-box; }
  html, body { width: 1200px; height: 1200px; overflow: hidden; }
  body {
    background: var(--stage);
    font-family: "PT Serif", Georgia, serif;
    position: relative;
  }
  .flyer {
    position: absolute;
    left: 220px; top: 50px;
    width: 760px; height: 1100px;
    background: var(--paper);
    overflow: hidden;
    box-shadow: 0 10px 30px rgba(0,0,0,.18);
  }
  .photo-area {
    position: absolute;
    left: 320px; top: 150px;
    width: 440px; height: 600px;
    background:
      radial-gradient(ellipse 38% 32% at 35% 32%, #e8c2a6 0%, rgba(232,194,166,0) 100%),
      radial-gradient(ellipse 32% 30% at 72% 28%, #efc9ad 0%, rgba(239,201,173,0) 100%),
      radial-gradient(ellipse 40% 30% at 78% 10%, #d2a877 0%, rgba(210,168,119,0) 100%),
      linear-gradient(180deg, #f1ede9 0%, #e9e3dc 55%, #ffffff 100%);
    -webkit-mask-image: linear-gradient(90deg, transparent 0%, #000 22%);
            mask-image: linear-gradient(90deg, transparent 0%, #000 22%);
  }
  .swoosh { position: absolute; left: 0; top: 0; width: 760px; height: 300px; }
  .brand {
    position: absolute; left: 48px; top: 110px;
    display: flex; align-items: center; gap: 12px;
  }
  .brand-dot { width: 22px; height: 22px; border-radius: 50%; background: var(--teal); }
  .brand-name { color: var(--teal); font-size: 34px; font-weight: 700; }
  .brand-tagline {
    position: absolute; left: 82px; top: 158px;
    color: var(--teal); font-size: 19px; letter-spacing: 4px; text-transform: uppercase;
  }
  .brand-credential {
    position: absolute; left: 82px; top: 188px;
    color: var(--teal); font-size: 10px; letter-spacing: 1px; text-transform: uppercase;
  }
  .mission {
    position: absolute; left: 110px; top: 345px; width: 300px;
    color: var(--teal); font-size: 22px; line-height: 1.12;
  }
  .divider { position: absolute; left: 0; top: 430px; width: 520px; height: 80px; }
  .specialties {
    position: absolute; left: 150px; top: 535px;
    color: var(--teal); font-size: 15px; font-weight: 700;
  }
  .specialties h2 { font-size: 15px; letter-spacing: 1px; margin-bottom: 10px; }
  .specialties ul { list-style: none; }
  .specialties li { margin-bottom: 6px; position: relative; }
  .specialties li::before { content: "•"; position: absolute; left: -12px; }
  .specialties li:nth-child(1) { margin-left: 0; }
  .specialties li:nth-child(2) { margin-left: 14px; }
  .specialties li:nth-child(3) { margin-left: 28px; }
  .specialties li:nth-child(4) { margin-left: 28px; }
  .specialties li:nth-child(5) { margin-left: 28px; }
  .specialties li:nth-child(6) { margin-left: 44px; }
  .specialties li:nth-child(7) { margin-left: 56px; }
  .specialties li:nth-child(8) { margin-left: 66px; }
  .footer-bands { position: absolute; left: 0; top: 720px; width: 760px; height: 380px; }
  .contact-phone {
    position: absolute; left: 300px; top: 836px;
    display: flex; align-items: center; gap: 12px;
    color: var(--paper); font-size: 30px; font-weight: 700;
  }
  .contact-mail {
    position: absolute; left: 560px; top: 850px;
    display: flex; align-items: center; gap: 8px;
    color: var(--paper); font-size: 11px;
  }
  .contact-address {
    position: absolute; left: 60px; top: 960px;
    display: flex; align-items: center; gap: 8px;
    color: var(--teal-dark); font-size: 12px;
  }
  .contact-web {
    position: absolute; left: 330px; top: 1030px;
    color: var(--paper); font-size: 21px; font-weight: 700;
  }
</style>
</head>
<body>
  <main class="flyer">
    <div class="photo-area" role="img" aria-label="Fotografia de um casal maduro sorridente abraçado"></div>

    <svg class="swoosh" viewBox="0 0 760 300" aria-hidden="true">
      <path d="M760 0 L700 0 C640 120 420 220 60 230 C260 250 560 210 760 70 Z" fill="var(--teal)"/>
      <path d="M20 250 C300 275 600 200 760 90" fill="none" stroke="var(--teal-light)" stroke-width="3"/>
    </svg>

    <div class="brand">
      <span class="brand-dot"></span>
      <span class="brand-name">Helena Moraes</span>
    </div>
    <p class="brand-tagline">Fisioterapia Pélvica</p>
    <p class="brand-credential">Fisioterapeuta • Crefito</p>

    <p class="mission">Trabalha na reabilitação e no equilíbrio da musculatura do assoalho pélvico em adultos e crianças.</p>

    <svg class="divider" viewBox="0 0 520 80" aria-hidden="true">
      <path d="M0 70 C150 60 330 40 520 5" fill="none" stroke="var(--teal)" stroke-width="5"/>
    </svg>

    <section class="specialties">
      <h2>ESPECIALIDADES:</h2>
      <ul>
        <li>Disfunções do Assoalho Pélvico</li>
        <li>Uroginecologia</li>
        <li>Síndrome da bexiga dolorosa</li>
        <li>Dor pélvica crônica</li>
        <li>Urologia</li>
        <li>Coloproctologia</li>
        <li>Nutrição</li>
        <li>Psicologia</li>
      </ul>
    </section>

    <svg class="footer-bands" viewBox="0 0 760 380" aria-hidden="true">
      <path d="M0 130 L760 20 L760 40 L0 150 Z" fill="var(--teal-light)"/>
      <path d="M0 160 L760 50 L760 215 L0 215 Z" fill="var(--teal)"/>
      <path d="M0 265 L760 265 L760 380 L0 380 Z" fill="var(--teal)"/>
      <path d="M0 258 L760 258 L760 262 L0 262 Z" fill="var(--teal-light)"/>
    </svg>

    <div class="contact-phone">
      <svg width="34" height="34" viewBox="0 0 34 34" aria-hidden="true">
        <circle cx="17" cy="17" r="15" fill="none" stroke="#fff" stroke-width="2"/>
        <path d="M12 10 l3 0 l1.5 4 l-2 1.5 a9 9 0 0 0 4 4 l1.5 -2 l4 1.5 l0 3 a2 2 0 0 1 -2 2 a14 14 0 0 1 -12 -12 a2 2 0 0 1 2 -2 z" fill="#fff"/>
      </svg>
      <span>(41) 3555-0142</span>
    </div>

    <div class="contact-mail">
      <svg width="16" height="16" viewBox="0 0 16 16" aria-hidden="true">
        <circle cx="8" cy="8" r="7" fill="none" stroke="#fff" stroke-width="1.5"/>
        <path d="M4.5 5.5 h7 v5 h-7 z M4.5 5.5 l3.5 3 l3.5 -3" fill="none" stroke="#fff" stroke-width="1"/>
      </svg>
      <span>clinicahelenamoraes@gmail.com</span>
    </div>

    <div class="contact-address">
      <svg width="16" height="20" viewBox="0 0 16 20" aria-hidden="true">
        <path d="M8 0 a7 7 0 0 1 7 7 c0 5 -7 13 -7 13 s-7 -8 -7 -13 a7 7 0 0 1 7 -7 z" fill="var(--teal-dark)"/>
        <circle cx="8" cy="7" r="2.5" fill="#fff"/>
      </svg>
      <span>Rua das Acácias, 480 - sala 702 - Centro</span>
    </div>

    <p class="contact-web">www.clinicahelenamoraes.com.br</p>
  </main>
</body>
</html>
```